PowerPoint Template

We would like new powerpoint template for our organization: Fjordvik Data Guild.
Enclosed you find our logo and old template.
Industry/Entity Type
Computer
Requirements
Must have
- 1. Logo
2. Footer (for autor)
3. Font: Variations of ARIAL

```html
<!DOCTYPE html>
<html lang="en">
<head>
<meta charset="utf-8">
<title>Fjordvik Data Guild – Title Slide</title>
<link rel="stylesheet" href="https://fonts.googleapis.com/css2?family=Dosis:wght@400;500&display=swap">
<style>
  :root {
    --paper: #ffffff;
    --dot-tone: #e4e4e4;
    --dot-fade: #f7f7f7;
    --brand-red: #ee1c25;
    --brand-teal: #1b7a6a;
    --text-grey: #6b6b6b;
    --name-grey: #333333;
    --mark-blue: #1f6fb5;
  }
  html, body {
    margin: 0;
    padding: 0;
    width: 1200px;
    height: 900px;
    overflow: hidden;
    background: var(--paper);
  }
  .slide {
    position: relative;
    width: 1200px;
    height: 900px;
    overflow: hidden;
    background: var(--paper);
    font-family: "Dosis", Arial, sans-serif;
  }
  .halftone-backdrop {
    position: absolute;
    inset: 0 0 57px 0;
    background:
      radial-gradient(ellipse 900px 700px at 10% 30%, var(--dot-tone) 0%, var(--dot-fade) 55%, transparent 80%),
      linear-gradient(90deg, #efefef 0%, #f8f8f8 45%, var(--paper) 75%);
  }
  .brand-lockup {
    position: absolute;
    left: 862px;
    top: 273px;
    width: 166px;
    display: flex;
    flex-direction: column;
    align-items: center;
  }
  .brand-square {
    width: 140px;
    height: 140px;
    background: var(--brand-red);
  }
  .brand-name {
    margin-top: 14px;
    font-size: 20px;
    font-weight: 500;
    color: var(--name-grey);
    white-space: nowrap;
  }
  .title-block {
    position: absolute;
    right: 38px;
    top: 488px;
    text-align: right;
  }
  .project-title {
    margin: 0;
    font-size: 56px;
    font-weight: 400;
    line-height: 1;
    color: var(--brand-red);
  }
  .project-summary {
    margin: 20px 0 0;
    font-size: 30px;
    font-weight: 400;
    line-height: 48px;
    color: var(--text-grey);
  }
  .footer-rule {
    position: absolute;
    left: 0;
    right: 0;
    bottom: 57px;
    height: 7px;
    background: var(--brand-teal);
  }
  .footer-band {
    position: absolute;
    left: 0;
    right: 0;
    bottom: 0;
    height: 57px;
    background: var(--brand-red);
  }
</style>
</head>
<body>
  <main class="slide">
    <div class="halftone-backdrop" role="img" aria-label="Soft grey halftone dot pattern curving across the left of the slide"></div>

    <div class="brand-lockup">
      <div class="brand-square"></div>
      <div class="brand-name">Fjordvik Data Guild</div>
    </div>

    <section class="title-block">
      <h1 class="project-title">Project Title Here</h1>
      <p class="project-summary">
        Lorem ipsum dolor sit ipsum lorem ipsum<br>
        dolor sit ipsum Lorem ipsum dolor sit ipsum<br>
        Lorem ipsum dolor sit ipsum
      </p>
    </section>

    <div class="footer-rule"></div>
    <footer class="footer-band"></footer>
  </main>
</body>
</html>
```